Biz Card & Stationary for Kids Indoor Play Space Company
Bramble Hollow
Biz Card & Stationary for Kids Indoor Play Space Company - Childcare
Creative Brief
Bright & Fun-filled
Marla Quint
Owner
7148 Garnet Ave. Ashbury Falls, OH 44712
marla.quint@bramblehollowplay.com
https://bramblehollowplay.com/
Would like the feel of the design to be consistent with our website. I will upload our logo. I will provide you with a biz phone # in a few days. If needed, our Logo Font is "Brady Bunch Remastered".
zestlark zestlark
1. In addition to biz cards design, we also want stationary design (letterhead and envelope). 2. We would like to see versions where our logo has a different tag line of "Indoor Play Center". Maybe this tag-line could be used on the front of the card and the original tag-line on the back of the card?

```html
<!DOCTYPE html>
<html lang="en">
<head>
<meta charset="utf-8">
<title>Bramble Hollow – Business Card</title>
<link rel="stylesheet" href="https://fonts.googleapis.com/css2?family=Fredoka:wght@600&family=Open+Sans:wght@400;600&display=swap">
<style>
  :root {
    --stage: #2e2e30;
    --card: #ffffff;
    --red: #e2242b;
    --blue: #1d4fa8;
    --ink: #4a4a4a;
    --rule: #c9c9c9;
    --photo-a: #e9d6c2;
    --photo-b: #b9c7d8;
    --photo-c: #e7b25c;
  }
  * { margin: 0; padding: 0; box-sizing: border-box; }
  html, body { width: 1200px; height: 961px; overflow: hidden; background: var(--stage); }
  .canvas { position: relative; width: 1200px; height: 961px; }

  .card {
    position: absolute;
    width: 620px; height: 360px;
    background: var(--card);
    box-shadow: 0 18px 40px rgba(0,0,0,.45);
    overflow: hidden;
  }

  /* Back of card */
  .card--back { left: 70px; top: 70px; border: 4px solid var(--red); }
  .card--back .photo-area { position: absolute; inset: 0; width: 100%; height: 100%; }
  .card--back .brand {
    position: absolute; left: 30px; bottom: 40px;
    font-family: "Fredoka", sans-serif; font-weight: 600;
    font-size: 36px; line-height: 1; color: var(--red);
  }
  .card--back .tagline {
    position: absolute; left: 32px; bottom: 18px;
    font-family: "Fredoka", sans-serif; font-weight: 600;
    font-size: 14px; color: var(--blue);
  }
  .card--back .web {
    position: absolute; right: 30px; bottom: 92px;
    font-family: "Open Sans", sans-serif; font-weight: 600;
    font-size: 14px; color: var(--red);
  }

  /* Front of card */
  .card--front { left: 510px; top: 530px; border-left: 4px solid var(--red); }
  .card--front .bands { position: absolute; inset: 0; width: 100%; height: 100%; }
  .card--front .logo { position: absolute; left: 44px; top: 140px; }
  .card--front .brand {
    font-family: "Fredoka", sans-serif; font-weight: 600;
    font-size: 33px; line-height: 1; color: var(--red);
    white-space: nowrap;
  }
  .card--front .tagline {
    margin-top: 5px; margin-left: 2px;
    font-family: "Fredoka", sans-serif; font-weight: 600;
    font-size: 14px; letter-spacing: .5px; color: var(--blue);
  }
  .divider {
    position: absolute; left: 322px; top: 52px;
    width: 1px; height: 150px; background: var(--rule);
  }
  .contact { position: absolute; left: 338px; top: 48px; font-family: "Open Sans", sans-serif; color: var(--ink); }
  .contact .name { font-size: 21px; font-weight: 600; color: var(--blue); line-height: 1.1; }
  .contact .role { font-size: 13px; color: var(--red); margin-bottom: 8px; }
  .contact .address { font-size: 12.5px; line-height: 1.45; margin-bottom: 8px; }
  .contact .line { display: flex; align-items: center; gap: 7px; font-size: 12.5px; line-height: 1.6; white-space: nowrap; }
  .contact .line svg { width: 11px; height: 11px; fill: var(--ink); flex: none; }
  .card--front .web {
    position: absolute; left: 170px; top: 287px;
    transform: rotate(-5.4deg);
    font-family: "Open Sans", sans-serif; font-weight: 600;
    font-size: 15px; letter-spacing: 1.5px; color: #fff;
    white-space: nowrap;
  }
</style>
</head>
<body>
<main class="canvas">

  <section class="card card--back" aria-label="Business card back">
    <svg class="photo-area" viewBox="0 0 612 352" preserveAspectRatio="none">
      <defs>
        <linearGradient id="photoTone" x1="0" y1="0" x2="1" y2="1">
          <stop offset="0" stop-color="var(--photo-b)"/>
          <stop offset=".55" stop-color="var(--photo-a)"/>
          <stop offset="1" stop-color="var(--photo-c)"/>
        </linearGradient>
      </defs>
      <path role="img" aria-label="Photo of toddlers playing with colourful toys in a bright indoor play room"
            fill="url(#photoTone)"
            d="M0 0 H612 V150 q-30 -10 -52 12 q-28 -22 -58 0 q-22 -16 -50 4 q-10 24 -40 26 q-6 30 -40 34 q-4 30 -38 32 q-8 32 -46 30 q-20 26 -58 16 q-28 22 -62 4 q-34 20 -70 -4 q-30 16 -58 -8 q-20 6 -40 -6 Z"/>
    </svg>
    <div class="brand">Bramble Hollow</div>
    <div class="tagline">Where Imagination Plays</div>
    <div class="web">www.bramblehollowplay.com</div>
  </section>

  <section class="card card--front" aria-label="Business card front">
    <svg class="bands" viewBox="0 0 616 360" preserveAspectRatio="none" aria-hidden="true">
      <polygon points="0,330 616,268 616,282 0,344" fill="var(--red)"/>
      <polygon points="0,300 616,240 616,278 0,338" fill="var(--blue)"/>
      <polygon points="470,250 616,236 616,218 500,229" fill="var(--red)"/>
      <rect x="440" y="240" width="26" height="26" fill="var(--blue)"/>
    </svg>

    <div class="logo">
      <div class="brand">Bramble Hollow</div>
      <div class="tagline">Indoor Play Center</div>
    </div>

    <div class="divider"></div>

    <div class="contact">
      <div class="name">Marla Quint</div>
      <div class="role">Owner</div>
      <div class="address">7148 Garnet Ave.<br>Ashbury Falls, OH 44712</div>
      <div class="line">
        <svg viewBox="0 0 24 24"><path d="M6.6 10.8a15.2 15.2 0 0 0 6.6 6.6l2.2-2.2c.3-.3.7-.4 1-.2 1.1.4 2.3.6 3.6.6.6 0 1 .4 1 1V20c0 .6-.4 1-1 1A17 17 0 0 1 3 4c0-.6.4-1 1-1h3.5c.6 0 1 .4 1 1 0 1.3.2 2.5.6 3.6.1.3 0 .7-.2 1z"/></svg>
        330-555-0142
      </div>
      <div class="line">
        <svg viewBox="0 0 24 24"><path d="M7 1h10a2 2 0 0 1 2 2v18a2 2 0 0 1-2 2H7a2 2 0 0 1-2-2V3a2 2 0 0 1 2-2zm0 3v14h10V4zm5 15.5a1.2 1.2 0 1 0 0 2.4 1.2 1.2 0 0 0 0-2.4z"/></svg>
        330-555-0187
      </div>
      <div class="line">
        <svg viewBox="0 0 24 24"><path d="M2 5h20v14H2zm2 2v.5l8 5 8-5V7zm0 2.8V17h16V9.8l-8 5z"/></svg>
        marla.quint@bramblehollowplay.com
      </div>
    </div>

    <div class="web">www.bramblehollowplay.com</div>
  </section>

</main>
</body>
</html>
```